Hello there!
I am looking to have a label created for a jojoba oil product I am launching. I have attached the logo of my company below. The label should have the following information on it as well:
Ingredients: pure jojoba oil
Size of the bottle: 118ml
And there might be more but I am working on this and will keep you posted.

```html
<!DOCTYPE html>
<html lang="en">
<head>
<meta charset="utf-8">
<title>Meadowlark Hair Atelier – Pure Jojoba Oil Label</title>
<link rel="stylesheet" href="https://fonts.googleapis.com/css2?family=Gelasio:wght@400;700&family=Lato:wght@400&display=swap">
<style>
  :root {
    --page: #c3c6ce;
    --ink: #0c0c0c;
    --paper: #ffffff;
    --gold: #f6d936;
    --berry: #8e3522;
    --berry-light: #c9775e;
    --wood: #ecebea;
  }
  * { box-sizing: border-box; margin: 0; padding: 0; }
  html, body { width: 1200px; height: 524px; overflow: hidden; background: var(--page); }
  .label {
    position: absolute; left: 100px; top: 12px;
    width: 1000px; height: 500px; overflow: hidden;
    font-family: "Gelasio", Georgia, serif; color: var(--paper);
  }
  .label__backdrop {
    position: absolute; inset: 0;
    background:
      radial-gradient(ellipse 140px 110px at 60px 60px, var(--berry-light), transparent 70%),
      radial-gradient(ellipse 220px 200px at 780px 270px, var(--berry), transparent 72%),
      radial-gradient(ellipse 120px 90px at 920px 60px, var(--berry-light), transparent 70%),
      linear-gradient(180deg, #f7f6f5 0%, var(--wood) 100%);
  }
  .label__shapes { position: absolute; inset: 0; }
  .info-badge {
    position: absolute; text-align: center;
    font-size: 13px; line-height: 16px;
  }
  .info-badge--description { left: 34px; top: 106px; width: 165px; }
  .info-badge--description h2 { font-size: 13px; font-weight: 700; }
  .info-badge--details { left: 802px; top: 88px; width: 169px; }
  .info-badge--details h2 { font-size: 13px; font-weight: 400; }
  .info-badge--details p + h2 { margin-top: 16px; }
  .brand {
    position: absolute; left: 330px; top: 80px; width: 316px;
    text-align: center; color: var(--ink); font-weight: 400;
  }
  .brand__name { font-size: 46px; line-height: 52px; letter-spacing: 0.5px; }
  .brand__sub { font-size: 13px; letter-spacing: 9px; margin-top: 6px; padding-left: 9px; }
  .product-name {
    position: absolute; left: 274px; top: 207px; width: 428px;
    text-align: center; color: var(--gold); font-weight: 700;
  }
  .product-name__pure { font-size: 17px; line-height: 18px; }
  .product-name__main { font-size: 28px; line-height: 30px; }
  .tagline {
    position: absolute; left: 330px; top: 274px; width: 316px;
    text-align: center; color: var(--ink);
    font-size: 15px; line-height: 24px; letter-spacing: 3px;
  }
  .size-bar {
    position: absolute; left: 0; top: 450px; width: 1000px; height: 28px;
    text-align: center; font-family: "Lato", Arial, sans-serif;
    font-size: 17px; line-height: 28px;
  }
</style>
</head>
<body>
<main class="label">
  <div class="label__backdrop" role="img" aria-label="Photograph of ripe jojoba seeds and green leaves on a white wooden surface"></div>

  <svg class="label__shapes" viewBox="0 0 1000 500" width="1000" height="500" aria-hidden="true">
    <polygon fill="var(--ink)" points="26,98 116,86 207,98 207,306 116,318 26,306"/>
    <polygon fill="var(--ink)" points="796,80 887,67 977,80 977,430 887,443 796,430"/>
    <polygon fill="var(--paper)" stroke="var(--ink)" stroke-width="2" stroke-dasharray="6 3"
             points="332,67 488,52 644,67 644,404 488,418 332,404"/>
    <polygon fill="var(--ink)" points="274,198 702,198 650,231 702,264 274,264 326,231"/>
    <rect x="0" y="450" width="1000" height="28" fill="var(--ink)"/>
  </svg>

  <div role="img" aria-label="Photograph of a cluster of jojoba seeds with leaves"
       style="position:absolute;left:430px;top:320px;width:150px;height:95px;border-radius:50%;background:radial-gradient(ellipse at 50% 50%, #a23a26 0%, #c9634a 45%, rgba(255,255,255,0) 72%);"></div>

  <section class="info-badge info-badge--description">
    <h2>Product Description</h2>
    <p>Our premium Jojoba Oil is crafted to deeply nourish the scalp, reduce dryness, and promote a balanced, healthy environment for hair growth. With its lightweight, non-greasy formula, jojoba oil absorbs easily, delivering essential moisture to both scalp and hair.</p>
  </section>

  <header class="brand">
    <div class="brand__name">Meadowlark</div>
    <div class="brand__sub">HAIR ATELIER</div>
  </header>

  <h1 class="product-name">
    <span class="product-name__pure" style="display:block">PURE</span>
    <span class="product-name__main" style="display:block">JOJOBA OIL</span>
  </h1>

  <p class="tagline">Revitalize Your Scalp<br>Rejuvenate Your Hair</p>

  <section class="info-badge info-badge--details">
    <h2>Directions</h2>
    <p>Apply a few drops to the scalp, massaging gently. For a deeper treatment, leave on for 20 minutes before rinsing, or leave overnight for intense hydration. Use 1-2 times per week for optimal results.</p>
    <h2>Ingredients</h2>
    <p>100% Pure Jojoba Oil (Simmondsia Chinensis)</p>
    <h2>Caution</h2>
    <p>For external use only. Avoid contact with eyes. Discontinue use if irritation occurs. Store in a cool, dry place.</p>
  </section>

  <div class="size-bar">118ml / 4 fl oz</div>
</main>
</body>
</html>
```